Business Cards for a law firm

Business cards for our law firm. Use our silhoette logo and OAK HARBOR - check our website (www.oakharbor-legal.com)

Contact Information for Business Card

our silhouette logo, OAK HARBOR, 800-555-0147, Dorian Kestrup, dorian@oakharbor-legal.com

Requirements
Must have
• our silhouette logo, OAK HARBOR, 800-555-0147, Dorian Kestrup, dorian@oakharbor-legal.com

```html
<!DOCTYPE html>
<html lang="en">
<head>
<meta charset="utf-8">
<title>Oak Harbor Business Cards</title>
<link href="https://fonts.googleapis.com/css2?family=Montserrat:wght@400;600;700&family=Tenor+Sans&display=swap" rel="stylesheet">
<style>
  :root {
    --navy: #22316b;
    --white: #ffffff;
    --ink: #1f1f24;
    --stage: #2a2a2d;
  }
  html, body {
    margin: 0;
    padding: 0;
    width: 1200px;
    height: 900px;
    overflow: hidden;
    background: var(--stage);
  }
  .canvas {
    position: relative;
    width: 1200px;
    height: 900px;
  }
  .card {
    position: absolute;
    left: 260px;
    width: 680px;
    height: 388px;
    border-radius: 22px;
    overflow: hidden;
    box-shadow: 0 8px 20px rgba(0,0,0,0.45);
  }
  .card--back {
    top: 50px;
    background: var(--navy);
  }
  .card--front {
    top: 462px;
    background: var(--white);
  }
  .brand {
    position: absolute;
    display: flex;
    align-items: center;
    gap: 18px;
    font-family: "Tenor Sans", sans-serif;
    letter-spacing: 0.08em;
    white-space: nowrap;
  }
  .brand__mark {
    display: block;
    width: 22px;
    height: 22px;
  }
  .card--back .brand {
    left: 0;
    right: 0;
    top: 150px;
    justify-content: center;
    font-size: 52px;
    color: var(--white);
  }
  .card--back .brand__mark { background: var(--white); }
  .card--front .brand {
    left: 60px;
    top: 50px;
    font-size: 42px;
    color: var(--navy);
  }
  .card--front .brand__mark { background: var(--navy); }
  .person {
    position: absolute;
    left: 60px;
    top: 205px;
    padding-left: 28px;
  }
  .person__bar {
    position: absolute;
    left: 0;
    top: 4px;
    width: 8px;
    height: 36px;
    background: var(--navy);
  }
  .person__name {
    margin: 0;
    font-family: "Montserrat", sans-serif;
    font-weight: 700;
    font-size: 30px;
    color: var(--navy);
  }
  .person__title {
    margin: 2px 0 0;
    font-family: "Montserrat", sans-serif;
    font-size: 16px;
    color: var(--ink);
  }
  .contacts {
    position: absolute;
    left: 88px;
    top: 300px;
    margin: 0;
    padding: 0;
    list-style: none;
    font-family: "Montserrat", sans-serif;
    font-size: 16px;
    color: var(--ink);
  }
  .contacts li {
    display: flex;
    align-items: center;
    gap: 12px;
    line-height: 24px;
  }
  .contacts svg {
    width: 14px;
    height: 14px;
    fill: var(--navy);
  }
</style>
</head>
<body>
<div class="canvas">
  <section class="card card--back">
    <div class="brand"><span class="brand__mark"></span>OAK HARBOR</div>
  </section>

  <section class="card card--front">
    <div class="brand"><span class="brand__mark"></span>OAK HARBOR</div>

    <div class="person">
      <span class="person__bar"></span>
      <h1 class="person__name">Dorian Kestrup</h1>
      <p class="person__title">Attorney at Law</p>
    </div>

    <ul class="contacts">
      <li>
        <svg viewBox="0 0 16 16" aria-hidden="true"><path d="M3 1l3 3-2 2c1 2 4 5 6 6l2-2 3 3-2 2C7 15 1 9 1 3z"/></svg>
        800-555-0147
      </li>
      <li>
        <svg viewBox="0 0 16 16" aria-hidden="true"><path d="M1 3h14v10H1z M1 3l7 6 7-6" fill="none" stroke="#22316b" stroke-width="1.6"/></svg>
        dorian@oakharbor-legal.com
      </li>
      <li>
        <svg viewBox="0 0 16 16" aria-hidden="true"><circle cx="8" cy="8" r="6.5" fill="none" stroke="#22316b" stroke-width="1.6"/><path d="M1.5 8h13M8 1.5c-3 3.5-3 9.5 0 13M8 1.5c3 3.5 3 9.5 0 13" fill="none" stroke="#22316b" stroke-width="1.2"/></svg>
        www.oakharbor-legal.com
      </li>
    </ul>
  </section>
</div>
</body>
</html>
```